Powerpoint template for basic scientists studying immunology

We are an QFB-funded consortium of basic science researchers at academic centers in Boston, Philadelphia and Oxford, UK. We study why the immune system fails to get rid of Hepatitis C virus, and whether new antiviral treatments that reduce viral load improve immune function. We are looking for a powerpoint template that we can use as a "brand" for our research consortium. It would feature a logo (file attached) and should represent the fonts/colors contained in the logo. We we would present at meetings and to program officers at the QFB, but, if we ever get around to it, would also be on a website.

The scientific description is as follows:
Hepatitis C virus (HCV) infects 185 million persons worldwide, is the leading indication for liver transplantation and, in the US, has a higher mortaliy rate than HIV. The annual healthcare costs associated with HCV exceed $9 billion, a number expected to increase as the epidemic matures and end stage liver disease peaks over the next decade. By virtue of its remarkable predilection for persistence, HCV is a model chronic viral infection. Mounting evidence supports the idea that HCV, while inducing type I IFN expression, maintains chronicity by virtue of global suppression of host innate and adaptive immunity. The mainstay of treatment for the last two decades, IFN-α-based regimens are ineffective in many patient subgroups and have significant side effects. The recent development of highly effective direct acting antivirals (DAA) against HCV promises to alter the landscape of this devastating infection by offering curative therapy without IFN. However, it remains essential that we understand what type of immunity remains following pharmacological eradication of the virus because: a) many HCV infected subjects remain at risk for re-infection; and b) DAAs are only partially effective in some patient subgroups, particularly those with past treatment with IFN. The imminent availability of IFN-free treatment for HCV offers an unprecedented opportunity to understand broad questions about alterations in immunity in humans with cure of chronic infections. Until now, mechanistic dissection of human immune responses has been challenging due to limited ability to directly perturb the system. The organizing principle of this U19 Program therefore, is to capitalize on the unique opportunity to, for the first time, cure chronic viral infection in humans without immune modulation and interrogate the immunological changes that ensue. Thus, we have formulated the following central hypothesis for this Program: DAA-mediated cure of chronic HCV infection will lead to partial "resetting" of some immune abnormalities, but specific immunological defects will persist in some subjects that prevent development of optimal immunity to HCV. We will test this hypothesis through a set of integrated Projects and Cores.

Target Market(s)

scientists.

Industry/Entity Type

Biotechnology

Font styles to use
Sans Serif

Requirements
Must have
• Very clean, very simple. Mostly whitespace for puting graphs and data on. Colors, fonts should match the logo. Please see ppt example.
Should not have
• too much of the ppt covered with the logo.

```html
<!DOCTYPE html>
<html lang="en">
<head>
<meta charset="utf-8">
<title>Project Title Slide</title>
<link rel="stylesheet" href="https://fonts.googleapis.com/css2?family=Roboto+Condensed:wght@400;700&family=Roboto:wght@500&family=Open+Sans:wght@400;600&display=swap">
<style>
  :root {
    --brand-blue: #0a99cc;
    --table-blue: #0078b4;
    --row-grey: #e4e4e4;
    --row-blue: #c5e5f0;
    --body-grey: #9a9a9a;
    --footer-grey: #666666;
    --ink: #222222;
    --white: #ffffff;
  }
  * { box-sizing: border-box; margin: 0; padding: 0; }
  html, body { width: 1200px; height: 900px; overflow: hidden; background: var(--white); }
  .slide { position: relative; width: 1200px; height: 900px; background: var(--white); }

  .slide-header {
    position: absolute; left: 0; top: 0; width: 1200px; height: 96px;
    background: var(--brand-blue);
    display: flex; align-items: center; justify-content: space-between;
    padding: 0 30px 0 27px;
  }
  .project-title {
    font-family: "Roboto Condensed", sans-serif; font-weight: 700;
    font-size: 46px; color: var(--white); letter-spacing: 0.5px;
  }
  .brand { display: flex; align-items: center; gap: 14px; }
  .brand-dot { width: 40px; height: 40px; border-radius: 50%; background: var(--white); }
  .brand-name {
    font-family: "Roboto Condensed", sans-serif; font-weight: 400;
    font-size: 30px; color: var(--white); letter-spacing: 1px;
  }

  .section-heading {
    position: absolute; left: 24px; top: 160px;
    display: flex; align-items: center; gap: 22px;
  }
  .heading-dot { width: 44px; height: 44px; border-radius: 50%; background: var(--brand-blue); opacity: 0.85; }
  .heading-text {
    font-family: "Roboto", sans-serif; font-weight: 500;
    font-size: 30px; color: var(--brand-blue);
  }
  .section-intro {
    position: absolute; left: 102px; top: 206px; width: 1002px;
    font-family: "Roboto", sans-serif; font-weight: 500;
    font-size: 17.5px; line-height: 24.5px; color: var(--body-grey);
  }

  .data-table {
    position: absolute; left: 100px; top: 320px; width: 1008px;
    display: grid; grid-template-columns: 340px 392px 276px;
    grid-auto-rows: 60px; row-gap: 4px;
    font-family: "Open Sans", sans-serif;
  }
  .data-table .head {
    background: var(--table-blue); color: var(--white);
    font-weight: 600; font-size: 25px; text-transform: uppercase;
    display: flex; align-items: center; padding-left: 22px;
  }
  .data-table .cell {
    font-size: 19px; color: var(--ink);
    display: flex; align-items: center; padding-left: 26px;
  }
  .data-table .row-grey { background: var(--row-grey); }
  .data-table .row-blue { background: var(--row-blue); }

  .slide-footer {
    position: absolute; left: 0; bottom: 0; width: 1200px; height: 50px;
    background: var(--footer-grey);
    display: flex; align-items: center; justify-content: space-between;
    padding: 0 12px;
    font-family: "Roboto Condensed", sans-serif; font-size: 21px; color: var(--white);
  }
</style>
</head>
<body>
<div class="slide">
  <header class="slide-header">
    <h1 class="project-title">PROJECT TITLE HERE</h1>
    <div class="brand">
      <span class="brand-dot"></span>
      <span class="brand-name">ARVIN CONSORTIUM</span>
    </div>
  </header>

  <div class="section-heading">
    <span class="heading-dot"></span>
    <h2 class="heading-text">Table Head Here</h2>
  </div>
  <p class="section-intro">Lorem ipsum dolor sit Lorem ipsum dolor sit&nbsp; Lorem ipsum dolor sit Lorem ipsum dolor sit&nbsp; Lorem ipsum dolor sit Lorem ipsum dolor&nbsp; Lorem ipsum dolor sit Lorem ipsum dolor sit&nbsp; Lorem ipsum dolor sit Lorem ipsum dolor sit&nbsp; Lorem ipsum dolor sit Lorem ipsum dolor&nbsp; Lorem ipsum dolor sit Lorem ipsum dolor sit&nbsp; Lorem ipsum dolor sit Lorem ipsum dolor sit</p>

  <div class="data-table" role="table">
    <div class="head">Table Head Here</div>
    <div class="head">Table Head Here</div>
    <div class="head">Table Head Here</div>

    <div class="cell row-grey">Subtext here Subtext here</div>
    <div class="cell row-grey">Subtext here Subtext here</div>
    <div class="cell row-grey">Subtext here Subtext here</div>

    <div class="cell row-blue">Subtext here Subtext here</div>
    <div class="cell row-blue">Subtext here Subtext here</div>
    <div class="cell row-blue">Subtext here Subtext here</div>

    <div class="cell row-grey">Subtext here Subtext here</div>
    <div class="cell row-grey">Subtext here Subtext here</div>
    <div class="cell row-grey">Subtext here Subtext here</div>

    <div class="cell row-blue">Subtext here Subtext here</div>
    <div class="cell row-blue">Subtext here Subtext here</div>
    <div class="cell row-blue">Subtext here Subtext here</div>

    <div class="cell row-grey">Subtext here Subtext here</div>
    <div class="cell row-grey">Subtext here Subtext here</div>
    <div class="cell row-grey">Subtext here Subtext here</div>

    <div class="cell row-blue">Subtext here Subtext here</div>
    <div class="cell row-blue">Subtext here Subtext here</div>
    <div class="cell row-blue">Subtext here Subtext here</div>
  </div>

  <footer class="slide-footer">
    <span class="copyright">Copyright text here</span>
    <span class="page-number">Page : 01</span>
  </footer>
</div>
</body>
</html>
```